Hallo,
ich benötige für ein bereits fertiges Cover noch einige Grafiken um das Buch auf SociaMedia zu bewerben.
Nachdem es sich um einen Erotikroman handelt, geschrieben aus der Sicht eines Mannes, gehe ich davon aus, das das hauptsächlich Männer interessieren wird.
Es handelt sich um folgenden Roman: https://www.buchkiste-online.de/dp/X7QRTZ4K2M
Aufgabenstellung
Die benötigten Grafiken im einzelnen:
* Hochformat: 660 x 1173 Pixel
* Quadratisch: 1080 Pixel
* Querformat: 1173 x 660 Pixel
Die Bilder sollten beinhalten:
* Das Cover
* Der Text 'Jetzt im Handel' und 'Zum Einführungspreis von xx%'
* Die Beschreibung des Buches sollte gut lesbar vorkommen:
Eines Tages kauft der Student Kilian ein neuartiges Online-Computerspiel und weiß zu diesem Zeitpunkt noch nicht, dass sich sein Sex-Leben dadurch drastisch verbessern wird.

```html
<!DOCTYPE html>
<html lang="de">
<head>
<meta charset="utf-8">
<title>Fantasy &amp; Erotik Roman – Jetzt im Handel</title>
<link rel="stylesheet" href="https://fonts.googleapis.com/css2?family=Arimo:wght@400;700&display=swap">
<style>
  :root {
    --fog-top: #5f8593;
    --fog-mid: #9fc3cf;
    --fog-low: #dfe8ea;
    --fog-bottom: #eef2f2;
    --price-panel: rgba(78, 84, 88, 0.78);
    --badge-fill: #6fb1c6;
    --badge-ring: #14191c;
    --ink: #0c0c0c;
    --white: #ffffff;
    --device-bezel: #121416;
    --device-edge: #5a5e62;
    --cover-dark: #2b3236;
    --cover-mid: #6f7a7c;
    --cover-light: #b9c2c0;
  }
  * { margin: 0; padding: 0; box-sizing: border-box; }
  html, body { width: 1200px; height: 1200px; overflow: hidden; }
  body { font-family: "Arimo", Arial, sans-serif; }

  .ad {
    position: relative;
    width: 1200px;
    height: 1200px;
    overflow: hidden;
  }
  .forest-backdrop {
    position: absolute; inset: 0;
    background:
      radial-gradient(ellipse at 70% 80%, rgba(255,255,255,0.55), transparent 60%),
      linear-gradient(180deg, var(--fog-top) 0%, var(--fog-mid) 35%, var(--fog-low) 70%, var(--fog-bottom) 100%);
  }

  .price-panel {
    position: absolute;
    left: 177px; top: 110px;
    width: 528px; height: 288px;
    background: var(--price-panel);
    border-radius: 12px;
  }
  .price-intro {
    position: absolute;
    left: 226px; top: 142px;
    color: var(--white);
    font-size: 46px;
    line-height: 59px;
    font-weight: 400;
  }
  .price-amount {
    position: absolute;
    left: 326px; top: 278px;
    color: var(--white);
    font-size: 90px;
    font-weight: 700;
    line-height: 1;
    letter-spacing: -1px;
  }
  .price-currency {
    position: absolute;
    left: 510px; top: 282px;
    color: var(--white);
    font-size: 40px;
    font-weight: 700;
    line-height: 1;
  }

  .badge {
    position: absolute;
    left: 44px; top: 328px;
    width: 282px; height: 282px;
    border-radius: 50%;
    background: var(--badge-fill);
    border: 3px solid var(--badge-ring);
    box-shadow: 0 0 0 6px var(--badge-fill), 0 0 0 8px rgba(0,0,0,0.0);
    display: flex; align-items: center; justify-content: center;
  }
  .badge-text {
    transform: rotate(-9deg);
    text-align: center;
    color: var(--ink);
    font-size: 48px;
    font-weight: 700;
    line-height: 58px;
  }

  .tablet {
    position: absolute;
    left: 705px; top: 70px;
    width: 450px; height: 589px;
    background: var(--device-bezel);
    border: 2px solid var(--device-edge);
    border-radius: 30px;
    box-shadow: 0 6px 14px rgba(0,0,0,0.35);
  }
  .tablet-screen {
    position: absolute;
    left: 18px; top: 18px; right: 18px; bottom: 18px;
    border-radius: 10px;
    background: linear-gradient(180deg, var(--cover-light) 0%, var(--cover-mid) 45%, var(--cover-dark) 100%);
  }
  .phone {
    position: absolute;
    left: 592px; top: 265px;
    width: 193px; height: 396px;
    background: var(--device-bezel);
    border: 2px solid var(--device-edge);
    border-radius: 26px;
    box-shadow: 0 6px 14px rgba(0,0,0,0.35);
  }
  .phone-screen {
    position: absolute;
    left: 8px; top: 8px; right: 8px; bottom: 8px;
    border-radius: 20px;
    background: linear-gradient(180deg, var(--cover-light) 0%, var(--cover-mid) 45%, var(--cover-dark) 100%);
  }
  .phone-notch {
    position: absolute;
    left: 50%; top: 8px;
    width: 76px; height: 16px;
    transform: translateX(-50%);
    background: var(--device-bezel);
    border-radius: 0 0 10px 10px;
  }

  .headline {
    position: absolute;
    left: 91px; top: 738px;
    width: 1030px;
    color: var(--ink);
    font-size: 47px;
    font-weight: 700;
    line-height: 59px;
    letter-spacing: 0.2px;
  }
  .blurb {
    position: absolute;
    left: 91px; top: 866px;
    width: 1021px;
    color: var(--ink);
    font-size: 47px;
    font-weight: 400;
    line-height: 58px;
    text-align: justify;
    hyphens: auto;
  }
</style>
</head>
<body>
  <main class="ad">
    <div class="forest-backdrop" role="img" aria-label="Nebliger Wald in kühlen Blau- und Grautönen als Hintergrund"></div>

    <div class="price-panel"></div>
    <p class="price-intro">Zum<br>Einführungspreis<br>von</p>
    <p class="price-amount">-,99</p>
    <p class="price-currency">€</p>

    <div class="badge">
      <p class="badge-text">Jetzt im<br>Handel!</p>
    </div>

    <div class="tablet">
      <div class="tablet-screen" role="img" aria-label="Buchcover des Romans auf einem Tablet: Fantasy-Heldin mit Kapuze im Wald, Autorname und Titel"></div>
    </div>
    <div class="phone">
      <div class="phone-screen" role="img" aria-label="Buchcover des Romans auf einem Smartphone, mit Genreangabe Fantasy, Erotik"></div>
      <div class="phone-notch"></div>
    </div>

    <h1 class="headline">DER NEUE FANTASY &amp; EROTIK ROMAN<br>VON KONRAD P. WALTERSHOFEN</h1>
    <p class="blurb">Eines Tages kauft der Student Kilian ein neuartiges Online-Computerspiel und weiß zu diesem Zeitpunkt noch nicht, dass sich sein Sex-Leben dadurch drastisch verbes&shy;sern wird.</p>
  </main>
</body>
</html>
```